Eco friendly Swedish beauty products sold in aluminum bottles - label design needed

We need help in designing a series of stick on labels for 80 ml (2.7 fl. oz.) aluminum bottles containing beauty products such as soaps, shampoo etc. The diameter of the bottle is 36 mm and the body of the bottles measures approx. 106 mm.
It is important for us that the label has a simplistic and clean feel with few colors (and the right ones!) and that the label helps amplify this product being both better and a more sustainable alternative to many of our plastic bottle competitors. The design and label should communicate the feel of an Eco-friendly, sustainable and modern brand of high quality - and with a Swedish concept.
We are using Montserrat font in our materials. Find attached information of preferred colors, the bottles and one example of our logotype. I am also available on e-mail should further information be needed.

Looking forward and very excited to receive your suggestions.
Note that we are expecting to start selling a series of approximately 10 different products where I will need one "master design" and then only smaller changes for each of the different products.

Target Market(s)

People whom are aware and not only look at price tag. Private and commercial market.

Industry/Entity Type

Beauty

Font styles to use
Other font styles liked:
• Montserrat

Requirements
Must have
• It must give the feel of being both better and a more sustainable alternative to many of our plastic bottle competitors.
Nice to have
• Simplistic. Clean. Clear.
Should not have
• Wrong colors, too complex designs.

```html
<!DOCTYPE html>
<html lang="en">
<head>
<meta charset="utf-8">
<title>Norrvik Body Lotion – Label Series</title>
<link href="https://fonts.googleapis.com/css2?family=Montserrat:wght@400;500&display=swap" rel="stylesheet">
<style>
  :root{
    --canvas:#efebe6;
    --cream:#f4efe6;
    --olive:#6e7a3a;
    --stone:#dcd9d6;
    --rust:#9c4a32;
    --peach:#dfb79c;
    --charcoal:#333333;
    --ochre:#a8641c;
    --copper:#a0622a;
    --amber:#d98a2a;
    --ink:#1e1e1e;
    --white:#ffffff;
    --brand-ink:#3a2b22;
  }
  *{box-sizing:border-box;margin:0;padding:0}
  html,body{width:1200px;height:812px;overflow:hidden}
  body{background:var(--canvas);font-family:"Montserrat",sans-serif;position:relative}

  .wordmark{position:absolute;left:880px;top:78px;display:flex;align-items:center;gap:14px;
    color:var(--brand-ink);font-weight:400;font-size:40px;letter-spacing:.14em}
  .wordmark .dot{width:18px;height:18px;border-radius:50%;background:var(--brand-ink)}

  .label{position:absolute;background:var(--bg);color:var(--fg);overflow:hidden;
    --title:13.5px;--small:8.5px;--tiny:7.5px;--mark-size:9px}
  .label > div{position:absolute;left:0;right:0;text-align:center;transform:translateY(-50%);white-space:nowrap}
  .label .brand{top:11%;display:flex;justify-content:center;align-items:center;gap:.45em;
    font-size:var(--mark-size);letter-spacing:.1em;color:var(--mark,var(--fg));transform:translateY(-50%)}
  .label .brand .dot{width:.7em;height:.7em;border-radius:50%;background:currentColor}
  .label .product{top:49%;font-size:var(--title);letter-spacing:.03em}
  .label .tagline{top:86%;font-size:var(--small);line-height:1.05}
  .label .volume{top:94%;font-size:var(--tiny)}
  .label .sprig{top:auto;left:auto;right:5%;bottom:4%;width:42%;height:20%;transform:none;
    background:rgba(255,255,255,.07);border-radius:50% 50% 40% 40%}

  .flat{width:117px;height:344px}
  .bottle-md{--title:12.5px;--small:8px;--tiny:7px;--mark-size:9px}
  .bottle-lg{--title:13.5px;--small:8.5px;--tiny:7.5px;--mark-size:9.5px}
  .bottle-sm{--title:10px;--small:6.5px;--tiny:5.5px;--mark-size:7px}
  .bottle-xs{--title:7.5px;--small:5px;--tiny:4.5px;--mark-size:5.5px}

  .is-cream{--bg:var(--cream);--fg:var(--copper)}
  .is-olive{--bg:var(--olive);--fg:var(--ink)}
  .is-stone{--bg:var(--stone);--fg:var(--amber)}
  .is-rust{--bg:var(--rust);--fg:var(--white)}
  .is-peach{--bg:var(--peach);--fg:var(--ink)}
  .is-charcoal{--bg:var(--charcoal);--fg:var(--amber)}
  .is-olive-light{--bg:var(--olive);--fg:var(--white)}
  .is-rust-dark{--bg:var(--rust);--fg:var(--ink);--mark:var(--white)}
  .is-charcoal-light{--bg:var(--charcoal);--fg:var(--white)}
  .is-ochre{--bg:var(--ochre);--fg:var(--white)}
  .is-peach-copper{--bg:var(--peach);--fg:var(--copper)}
</style>
</head>
<body>

  <div class="wordmark"><span class="dot"></span><span>NORRVIK</span></div>

  <section class="label flat is-cream" style="left:18px;top:52px">
    <div class="brand"><span class="dot"></span>NORRVIK</div>
    <div class="product">BODY LOTION</div>
    <div class="tagline">fresh &amp; beauty<br>from nature</div>
    <div class="volume">80 mL (2.7 FL OZ)</div>
  </section>
  <section class="label flat is-olive" style="left:165px;top:52px">
    <div class="brand"><span class="dot"></span>NORRVIK</div>
    <div class="product">BODY LOTION</div>
    <div class="tagline">fresh &amp; beauty<br>from nature</div>
    <div class="volume">80 mL (2.7 FL OZ)</div>
  </section>
  <section class="label flat is-stone" style="left:315px;top:52px">
    <div class="brand"><span class="dot"></span>NORRVIK</div>
    <div class="product">BODY LOTION</div>
    <div class="tagline">fresh &amp; beauty<br>from nature</div>
    <div class="volume">80 mL (2.7 FL OZ)</div>
  </section>

  <section class="label flat is-rust" style="left:20px;top:435px">
    <div class="sprig" role="img" aria-label="Faint leafy sprig decoration"></div>
    <div class="brand"><span class="dot"></span>NORRVIK</div>
    <div class="product">BODY LOTION</div>
    <div class="tagline">fresh &amp; beauty<br>from nature</div>
    <div class="volume">80 mL (2.7 FL OZ)</div>
  </section>
  <section class="label flat is-peach" style="left:168px;top:435px">
    <div class="brand"><span class="dot"></span>NORRVIK</div>
    <div class="product">BODY LOTION</div>
    <div class="tagline">fresh &amp; beauty<br>from nature</div>
    <div class="volume">80 mL (2.7 FL OZ)</div>
  </section>
  <section class="label flat is-charcoal" style="left:302px;top:435px">
    <div class="brand"><span class="dot"></span>NORRVIK</div>
    <div class="product">BODY LOTION</div>
    <div class="tagline">fresh &amp; beauty<br>from nature</div>
    <div class="volume">80 mL (2.7 FL OZ)</div>
  </section>

  <section class="label bottle-md is-olive-light" style="left:475px;top:367px;width:113px;height:337px">
    <div class="sprig" role="img" aria-label="Faint leafy sprig decoration"></div>
    <div class="brand"><span class="dot"></span>NORRVIK</div>
    <div class="product" style="top:50%">BODY LOTION</div>
    <div class="tagline">fresh &amp; beauty<br>from nature</div>
    <div class="volume" style="top:93%">80 mL (2.7 FL OZ)</div>
  </section>
  <section class="label bottle-lg is-rust-dark" style="left:639px;top:340px;width:123px;height:364px">
    <div class="sprig" role="img" aria-label="Faint leafy sprig decoration"></div>
    <div class="brand"><span class="dot"></span>NORRVIK</div>
    <div class="product" style="top:54%">BODY LOTION</div>
    <div class="tagline" style="top:87%">fresh &amp; beauty<br>from nature</div>
    <div class="volume">80 mL (2.7 FL OZ)</div>
  </section>
  <section class="label bottle-md is-charcoal-light" style="left:815px;top:349px;width:113px;height:332px">
    <div class="sprig" role="img" aria-label="Faint leafy sprig decoration"></div>
    <div class="brand"><span class="dot"></span>NORRVIK</div>
    <div class="product" style="top:53%">BODY LOTION</div>
    <div class="tagline" style="top:87%">fresh &amp; beauty<br>from nature</div>
    <div class="volume">80 mL (2.7 FL OZ)</div>
  </section>
  <section class="label bottle-xs is-ochre" style="left:962px;top:575px;width:70px;height:202px">
    <div class="brand"><span class="dot"></span>NORRVIK</div>
    <div class="product" style="top:48%">BODY LOTION</div>
    <div class="tagline">fresh &amp; beauty<br>from nature</div>
    <div class="volume">80 mL (2.7 FL OZ)</div>
  </section>
  <section class="label bottle-sm is-peach-copper" style="left:1048px;top:506px;width:88px;height:265px">
    <div class="sprig" role="img" aria-label="Faint leafy sprig decoration"></div>
    <div class="brand"><span class="dot"></span>NORRVIK</div>
    <div class="product" style="top:50%">BODY LOTION</div>
    <div class="tagline">fresh &amp; beauty<br>from nature</div>
    <div class="volume">80 mL (2.7 FL OZ)</div>
  </section>

</body>
</html>
```